CorkGlow Artbook for Okanagan Region, British Columbia

Creating an art book: CorkGlow, for the Okanagan Wine Region in British Columbia, Canada. Would like smart, modern, clean and linear...cool, sexy urban, not ugly boring suburban... I need a cover that appeals to the wino in all of us! Title: CorkGlow -Marla Pendrick
Updates
Thank you all kindly for your efforts. I have added some files so that you can get a sense of my aesthetic...it's never easy trying to figure it out, is it? I will hopefully have dimensions of book soon...cheers, Marla
would anyone please design a giant wine bottle with the wine label that looks like a label but says corkglow...just curious to see if it works as a design or not...thank you.
Target Market(s)
Designing this wine art book of quotes to wineries in Okanagan BC. Buyer is wine lover and tourist ready to spend his vacation bucks on this wonderful book!
Look and feel

```html
<!DOCTYPE html>
<html lang="en">
<head>
<meta charset="utf-8">
<title>CorkGlow – Cover Options</title>
<link rel="stylesheet" href="https://fonts.googleapis.com/css2?family=Source+Sans+3:ital,wght@0,300;0,400;0,700;0,800;1,300&display=swap">
<style>
  :root {
    --board: #f4f4f4;
    --paper: #ffffff;
    --edge: #8f8f8f;
    --wine: #c2121f;
    --wine-deep: #8e0b15;
    --ink: #1a1a1a;
    --author: #9a9a9a;
    --glass-grey: #a4a4a4;
  }
  * { margin: 0; padding: 0; box-sizing: border-box; }
  html, body {
    width: 1200px; height: 726px; overflow: hidden;
    background: var(--board);
    font-family: "Source Sans 3", sans-serif;
  }
  .board { position: relative; width: 1200px; height: 726px; }

  .option-number {
    position: absolute; top: 96px;
    font-size: 22px; font-weight: 400; color: var(--ink);
  }

  .cover {
    position: absolute; top: 136px;
    width: 361px; height: 510px;
    background: var(--paper);
    border: 1px solid var(--edge);
    overflow: hidden;
  }
  .cover--one { left: 21px; }
  .cover--two { left: 422px; }
  .cover--three { left: 823px; }

  .author {
    position: absolute; top: 28px; right: 36px;
    font-size: 17px; font-weight: 400; color: var(--author);
    letter-spacing: 0.2px;
  }

  .title {
    position: absolute; right: 36px; bottom: 28px;
    writing-mode: vertical-rl; transform: rotate(180deg);
    font-size: 50px; line-height: 0.78; color: var(--wine);
    white-space: nowrap; letter-spacing: 0.5px;
  }
  .title__strong { font-weight: 800; }
  .title__light { font-weight: 300; font-style: italic; }

  .pour {
    position: absolute; top: 0; left: 152px;
    width: 5px; height: 272px; background: var(--wine);
  }

  .glass-art {
    position: absolute; top: 261px; height: 220px;
  }
  .glass-art--red {
    left: 83px; width: 102px;
    background: linear-gradient(180deg, #f3dfe0 0%, var(--wine) 35%, var(--wine-deep) 55%, #e8e8e8 100%);
  }
  .glass-art--grey {
    left: 92px; width: 80px;
    background: linear-gradient(180deg, #f0f0f0 0%, #dcdcdc 50%, var(--glass-grey) 100%);
  }
</style>
</head>
<body>
<main class="board">
  <span class="option-number" style="left:361px">1</span>
  <span class="option-number" style="left:762px">2</span>
  <span class="option-number" style="left:1162px">3</span>

  <section class="cover cover--one">
    <p class="author">Marla Pendrick</p>
    <div class="pour"></div>
    <div class="glass-art glass-art--red" role="img" aria-label="Illustration of red wine splashing into a slender wine glass"></div>
    <h1 class="title"><span class="title__strong">CORK</span><span class="title__light">GLOW</span></h1>
  </section>

  <section class="cover cover--two">
    <p class="author">Marla Pendrick</p>
    <div class="glass-art glass-art--grey" role="img" aria-label="Illustration of an empty outlined wine glass in grey"></div>
    <h1 class="title"><span class="title__strong">CORK</span><span class="title__light">GLOW</span></h1>
  </section>

  <section class="cover cover--three">
    <p class="author">Marla Pendrick</p>
    <h1 class="title"><span class="title__strong">CORK</span><span class="title__light">GLOW</span></h1>
  </section>
</main>
</body>
</html>
```